Copper Meadow Creamery Business cards

We need a logo design for our family dairy. Included on the cards should be my name/my husbands name/the dairy name/ all the phone numbers/address and email. The name is Copper Meadow Creamery, LLC. We would like to use our farm mascot pic on the card. We know the pictures I sent you are of a beef cow but she is the mascot of the farm. We were thinking that maybe put a picture of her head in the middle of the card with a "B" on one side and a "D" on the other side with a "C" around the picture of the cow. But we are open to any ideas. We are looking for something kind of professional and a design that that can be used on cards, clothing and a car sign. Black lettering and blue for the other color...or what looks good.

Target Market(s)

All

Industry/Entity Type

Farming

Contact Information for Business Card

Marla Dutton Owner (555)417-2093
Ronald Pfister Owner (555)238-7715
Copper Meadow Creamery, LLC (555)906-4182
Coppermeadowcreamery@mailbarn.test
7126 County Lane 91, Harlow Falls, IA 50917

Font styles to use
Sans Serif

Colors
3176b5
3c7bb8
3277b5
0255a3

Requirements
Must have
• Some design that incorporates a drawing/pic of the cow pictures that were sent.
Nice to have
• no suggestions
Should not have
• no suggestions

```html
<!DOCTYPE html>
<html lang="en">
<head>
<meta charset="utf-8">
<title>Copper Meadow Creamery – Business Cards</title>
<link rel="stylesheet" href="https://fonts.googleapis.com/css2?family=Crimson+Text&display=swap">
<style>
  :root {
    --page: #ffffff;
    --ink: #111111;
    --paper: #ffffff;
    --card-edge: #8a8a8a;
    --band-cool: #e7e8e9;
    --band-cream: #fdf9e6;
    --band-taupe: #e2ddd2;
    --band-silver: #f4f4f4;
    --band-sand: #dcd7c6;
    --night: #000000;
    --sky: #3bbfed;
    --on-dark: #ffffff;
  }
  * { margin: 0; padding: 0; box-sizing: border-box; }
  html, body {
    width: 1200px; height: 2390px; overflow: hidden;
    background: var(--page);
  }
  .sheet { position: relative; width: 1200px; height: 2390px; }

  .card {
    position: absolute; left: 3px; width: 1194px;
    border: 1.5px solid var(--card-edge);
    background: var(--paper);
    overflow: hidden;
  }
  .card--light  { top: 170px;  height: 664px; }
  .card--dark   { top: 943px;  height: 664px; }
  .card--sky    { top: 1724px; height: 666px; border-bottom: none; }

  .brand-band {
    position: absolute; left: 0; top: 0; width: 100%;
    display: flex; align-items: center; justify-content: center;
    background: linear-gradient(90deg, var(--band-cool) 0%, var(--band-cream) 24%,
      var(--band-taupe) 55%, var(--band-silver) 80%, var(--band-sand) 100%);
  }
  .card--light .brand-band { height: 331px; }
  .card--dark  .brand-band { height: 351px; }
  .card--sky   .brand-band { height: 374px; background: var(--paper); border-bottom: 1.5px solid var(--card-edge); }

  .brand__name {
    font-family: "Crimson Text", serif;
    font-size: 54px; line-height: 1; white-space: nowrap;
    color: var(--ink);
  }

  .contact {
    position: absolute; left: 0; width: 100%;
    font-family: "Crimson Text", serif;
    font-size: 31px; letter-spacing: -0.6px; color: var(--ink);
  }
  .card--light .contact { top: 0; }
  .card--dark  .contact { top: 351px; height: 313px; background: var(--night); color: var(--on-dark); }
  .card--sky   .contact { top: 374px; height: 292px; background: var(--sky); color: var(--on-dark); }

  .contact__line { position: absolute; white-space: nowrap; line-height: 1; }
  .contact__icon { position: absolute; width: 26px; height: 26px; }
  .contact__icon rect { fill: var(--ink); }
  .contact__icon path { fill: none; stroke: var(--paper); stroke-width: 2; stroke-linecap: round; stroke-linejoin: round; }
  .card--dark .contact__icon rect, .card--sky .contact__icon rect { fill: var(--on-dark); }
  .card--dark .contact__icon path { stroke: var(--night); }
  .card--sky  .contact__icon path { stroke: var(--sky); }
</style>
</head>
<body>
<main class="sheet">

  <section class="card card--light">
    <div class="brand-band">
      <p class="brand__name">Copper Meadow Creamery</p>
    </div>
    <div class="contact">
      <svg class="contact__icon" style="left:228px;top:448px" viewBox="0 0 26 26" aria-hidden="true"><rect width="26" height="26" rx="3"/><path d="M9 6c-2 2-2 9 2 13c2 2 4 2 6 1l-2-4-2 1c-1-1-2-4-2-6l2-1-1-4z"/></svg>
      <p class="contact__line" style="left:272px;top:428px">Marla Dutton (555) 417-2093 / Ronald Pfister (555) 238-7715</p>
      <p class="contact__line" style="left:278px;top:469px">Copper Meadow Creamery, LLC (555) 906-4182</p>
      <svg class="contact__icon" style="left:228px;top:520px" viewBox="0 0 26 26" aria-hidden="true"><rect width="26" height="26" rx="3"/><path d="M5 8h16v10H5zM5 8l8 6 8-6"/></svg>
      <p class="contact__line" style="left:278px;top:518px">Coppermeadowcreamery@mailbarn.test</p>
      <p class="contact__line" style="left:278px;top:565px">7126 County Lane 91, Harlow Falls, IA 50917</p>
    </div>
  </section>

  <section class="card card--dark">
    <div class="brand-band">
      <p class="brand__name">Copper Meadow Creamery</p>
    </div>
    <div class="contact">
      <svg class="contact__icon" style="left:238px;top:95px" viewBox="0 0 26 26" aria-hidden="true"><rect width="26" height="26" rx="3"/><path d="M9 6c-2 2-2 9 2 13c2 2 4 2 6 1l-2-4-2 1c-1-1-2-4-2-6l2-1-1-4z"/></svg>
      <p class="contact__line" style="left:283px;top:75px">Marla Dutton (555) 417-2093 / Ronald Pfister (555) 238-7715</p>
      <p class="contact__line" style="left:288px;top:116px">Copper Meadow Creamery, LLC (555) 906-4182</p>
      <svg class="contact__icon" style="left:238px;top:166px" viewBox="0 0 26 26" aria-hidden="true"><rect width="26" height="26" rx="3"/><path d="M5 8h16v10H5zM5 8l8 6 8-6"/></svg>
      <p class="contact__line" style="left:288px;top:164px">Coppermeadowcreamery@mailbarn.test</p>
      <p class="contact__line" style="left:288px;top:212px">7126 County Lane 91, Harlow Falls, IA 50917</p>
    </div>
  </section>

  <section class="card card--sky">
    <div class="brand-band">
      <p class="brand__name">Copper Meadow Creamery</p>
    </div>
    <div class="contact">
      <svg class="contact__icon" style="left:250px;top:94px" viewBox="0 0 26 26" aria-hidden="true"><rect width="26" height="26" rx="3"/><path d="M9 6c-2 2-2 9 2 13c2 2 4 2 6 1l-2-4-2 1c-1-1-2-4-2-6l2-1-1-4z"/></svg>
      <p class="contact__line" style="left:291px;top:72px">Marla Dutton (555) 417-2093 / Ronald Pfister (555) 238-7715</p>
      <p class="contact__line" style="left:296px;top:114px">Copper Meadow Creamery, LLC (555) 906-4182</p>
      <svg class="contact__icon" style="left:250px;top:166px" viewBox="0 0 26 26" aria-hidden="true"><rect width="26" height="26" rx="3"/><path d="M5 8h16v10H5zM5 8l8 6 8-6"/></svg>
      <p class="contact__line" style="left:296px;top:164px">Coppermeadowcreamery@mailbarn.test</p>
      <p class="contact__line" style="left:296px;top:212px">7126 County Lane 91, Harlow Falls, IA 50917</p>
    </div>
  </section>

</main>
</body>
</html>
```